BrightLoop Kiosk Business Card Design Project

BrightLoop Kiosk requires a business card design. We hire PhotoBooths to events such as Birthday Parties, Hens and Bucks Night, Anniversaries, Corporate Functions
, Engagements, Theme Nights, Presentation Night etc.
Business Card needs to look Modern, Professional And Catchy.
Updates

Hello Thankyou for all of your great designs, contact information will be provided shortly. We are considering the front of the card to be white themed and the back of the card to be black themed. And all social media colours to be their original colour. Thankyou

Hello everyone, Here are the contact details: Martin Colby - Manager Mobile number - 0491738205 Website - www.brightloopkiosk.example Email - admin@brightloopkiosk.example And if you can add the word "weddings" in the "We cater For" section would be good. Thankyou

Target Market(s)

Birthday Parties
Hens and Bucks Night
Weddings
Corporate Functions
Engagements
Theme Nights
Presentation Night
School Functions

Industry/Entity Type

Events

Requirements
Must have
• Must Match Logo
Must Have www.brightloopkiosk.example

On Back of card must have social media icons Facebook, Twitter, Youtube, Linkin and

We Cater For:

Birthday Parties
Hens and Bucks Night
Anniversaries
Corporate Functions
Engagements
Theme Nights
Presentation Night
School Functions
And more.....

```html
<!DOCTYPE html>
<html lang="en">
<head>
<meta charset="utf-8">
<title>BrightLoop Kiosk Business Card</title>
<link rel="stylesheet" href="https://fonts.googleapis.com/css2?family=Montserrat:wght@300;400;700&display=swap">
<style>
  :root {
    --brand-blue: #0bb0dc;
    --stage-blue: #12b1da;
    --paper: #ffffff;
    --ink: #111111;
  }
  * { margin: 0; padding: 0; box-sizing: border-box; }
  html, body { width: 1200px; height: 960px; overflow: hidden; }
  body {
    position: relative;
    font-family: "Montserrat", "Century Gothic", sans-serif;
    background: var(--paper);
  }
  .stage-lower {
    position: absolute; left: 0; top: 488px; width: 1200px; height: 472px;
    background: var(--stage-blue);
  }
  .card {
    position: absolute; left: 321px; width: 566px; height: 349px;
    overflow: hidden;
  }
  .card-front { top: 110px; background: var(--paper); }
  .card-back { top: 534px; background: var(--paper); }
  .card svg { position: absolute; inset: 0; width: 100%; height: 100%; }
  .front-band { fill: var(--brand-blue); }
  .front-frame { fill: none; stroke: var(--paper); stroke-width: 11; }
  .back-frame { fill: none; stroke: var(--brand-blue); stroke-width: 9; }

  .brand-lockup {
    position: absolute; left: 0; top: 116px; width: 100%; height: 123px;
    display: flex; align-items: center; justify-content: center; gap: 16px;
  }
  .brand-mark { width: 34px; height: 34px; background: var(--brand-blue); }
  .brand-name {
    font-weight: 400; font-size: 38px; color: var(--ink); letter-spacing: 1px;
  }

  .back-text {
    position: absolute; left: 6px; width: 100%; text-align: center;
    color: var(--brand-blue); font-weight: 300;
  }
  .contact-name { top: 45px; font-size: 13px; line-height: 17px; }
  .contact-address { top: 63px; font-size: 13px; line-height: 17px; }
  .cater-heading { top: 88px; font-size: 15px; font-weight: 700; line-height: 18px; }
  .cater-list { top: 104px; font-size: 15.5px; line-height: 14.9px; list-style: none; letter-spacing: 0.3px; }
  .contact-phone { top: 249px; font-size: 13px; line-height: 16px; }
  .contact-web { top: 263px; font-size: 13px; line-height: 16px; }
  .social-row {
    position: absolute; left: 0; top: 284px; width: 100%;
    display: flex; justify-content: center; gap: 6px; padding-left: 12px;
  }
  .social-slot { width: 21px; height: 20px; background: var(--brand-blue); }
</style>
</head>
<body>
  <div class="stage-lower"></div>

  <section class="card card-front">
    <svg viewBox="0 0 707 436" preserveAspectRatio="none" aria-hidden="true">
      <rect class="front-band" x="0" y="0" width="707" height="145"/>
      <rect class="front-band" x="0" y="298" width="707" height="138"/>
      <polyline class="front-frame" points="72,125 72,48 158,48"/>
      <polyline class="front-frame" points="550,46 637,46 637,121"/>
      <polyline class="front-frame" points="148,145 148,102 208,102"/>
      <polyline class="front-frame" points="483,102 542,102 542,145"/>
      <polyline class="front-frame" points="143,298 143,349 203,349"/>
      <polyline class="front-frame" points="480,349 541,349 541,298"/>
      <polyline class="front-frame" points="63,326 63,403 151,403"/>
      <polyline class="front-frame" points="547,407 633,407 633,331"/>
    </svg>
    <div class="brand-lockup">
      <span class="brand-mark"></span>
      <span class="brand-name">BrightLoop Kiosk</span>
    </div>
  </section>

  <section class="card card-back">
    <svg viewBox="0 0 707 436" preserveAspectRatio="none" aria-hidden="true">
      <polyline class="back-frame" points="99,123 99,53 179,53"/>
      <polyline class="back-frame" points="192,147 192,100 245,100"/>
      <polyline class="back-frame" points="543,50 623,50 623,121"/>
      <polyline class="back-frame" points="486,99 538,99 538,144"/>
      <polyline class="back-frame" points="188,270 188,318 240,318"/>
      <polyline class="back-frame" points="483,320 536,320 536,273"/>
      <polyline class="back-frame" points="91,311 91,382 172,382"/>
      <polyline class="back-frame" points="539,386 619,386 619,315"/>
    </svg>
    <p class="back-text contact-name">John Doe</p>
    <p class="back-text contact-address">Address:</p>
    <h2 class="back-text cater-heading">We Cater For:</h2>
    <ul class="back-text cater-list">
      <li>Birthday Parties</li>
      <li>Hens and Bucks Night</li>
      <li>Anniversaries</li>
      <li>Corporate Functions</li>
      <li>Engagements</li>
      <li>Theme Nights</li>
      <li>Presentation Night</li>
      <li>School Functions</li>
      <li>And more.....</li>
    </ul>
    <p class="back-text contact-phone">Phone:xxx.xxx.xxx</p>
    <p class="back-text contact-web">www.brightloopkiosk.example</p>
    <div class="social-row">
      <span class="social-slot"></span>
      <span class="social-slot"></span>
      <span class="social-slot"></span>
      <span class="social-slot"></span>
    </div>
  </section>
</body>
</html>
```